Fenwick Partners - Client Appreciation Party Invitation and Poster

We need a printable invitation, a version of the same invitation that can be emailed out, and also a Poster of the invitation for our annual client appreciation party.

The location is called: The Larkspur Loft. Here is a link to the location: https://www.thelarkspurloftvenue.com/

We like their font and their little logo that you see when you log onto this page. But we'd love to see creatively what you can come up with.

This party is for our clients who are interior designers and owners in the Hospitality industry. Here are the details which need to be included in the invitation:

Location: The Larkspur Loft - 482 W Tamsin Ave. Chicago IL 60618
Date/Time: Thursday August 23rd - 5:30-9:00pm
RSVP: Please RSVP to: gathering@fenwickpartners.com

Then our Sponsors Logos need to be included on the bottom: I have uploaded those logos here as well as our Logo and a copy of the invitation we did for last year's party so you can see sort of what we've done in the past.

For the poster - we typically do a version of the invitation (see uploaded example of last year's poster) with the sponsor logos and the overall theme of the invitation just a bit simplified by removing the date/time/location info. We need this in a printable format which can be blown up to a 24x30 poster size.

Requirements
Must have
• use 2 to 3 colors only.
• logos of sponsors can be of the same color.

```html
<!DOCTYPE html>
<html lang="en">
<head>
<meta charset="utf-8">
<title>Fenwick Partners – Weekend Warm Up</title>
<link rel="stylesheet" href="https://fonts.googleapis.com/css2?family=Playfair+Display:wght@700;800&family=Yellowtail&family=Montserrat:wght@600;700&display=swap">
<style>
  :root {
    --parchment: #efe5cc;
    --parchment-deep: #e2d4b2;
    --foliage: #9fae9c;
    --forest: #25473a;
    --rust: #8a4a34;
    --navy: #1e3a62;
    --ink: #2a2622;
    --frame: #7f9585;
    --white: #ffffff;
  }
  * { margin: 0; padding: 0; box-sizing: border-box; }
  html, body { width: 776px; height: 1200px; overflow: hidden; }
  body {
    position: relative;
    background: radial-gradient(ellipse at 50% 45%, #f3ebd6 0%, var(--parchment) 55%, var(--parchment-deep) 100%);
    font-family: "Montserrat", Arial, sans-serif;
    color: var(--ink);
  }
  .foliage {
    position: absolute;
    border-radius: 50%;
    background: radial-gradient(closest-side, rgba(159,174,156,0.45), rgba(159,174,156,0));
  }
  .foliage--top-left { left: -80px; top: -60px; width: 300px; height: 260px; }
  .foliage--top-right { right: -70px; top: -50px; width: 320px; height: 300px; }
  .foliage--left { left: -90px; top: 640px; width: 220px; height: 360px; }
  .foliage--bottom-right { right: -60px; top: 800px; width: 220px; height: 300px; }
  .foliage--under-frame { left: 120px; top: 820px; width: 520px; height: 90px; }

  .host {
    position: absolute; top: 42px; left: 0; width: 100%;
    text-align: center;
    font-family: "Playfair Display", Georgia, serif;
    font-weight: 800; font-size: 35px; letter-spacing: 1px;
    color: var(--forest);
  }
  .event-title {
    position: absolute; left: 0; width: 100%;
    font-family: "Yellowtail", cursive;
    color: var(--rust);
    line-height: 1;
  }
  .event-title__line--one { top: 102px; left: 180px; font-size: 92px; }
  .event-title__line--two { top: 185px; left: 230px; font-size: 104px; }

  .photo-frame {
    position: absolute; left: 47px; top: 307px; width: 683px; height: 545px;
    background: var(--frame);
  }
  .photo {
    position: absolute; left: 13px; top: 11px; width: 658px; height: 522px;
    background:
      linear-gradient(180deg, #3c3a36 0%, #cfcac0 22%, #8b857a 45%, #7a5a3d 58%, #4a3038 78%, #2d2026 100%);
  }
  .photo__caption {
    position: absolute; left: 0; right: 0; top: 352px;
    text-align: center;
    font-family: "Playfair Display", Georgia, serif;
    font-weight: 700; font-size: 50px; line-height: 50px;
    color: var(--white); letter-spacing: 0.5px;
    padding-left: 40px;
  }

  .details { position: absolute; left: 0; width: 100%; text-align: center; }
  .venue { top: 866px; font-size: 30px; font-weight: 700; color: var(--navy); }
  .address { top: 917px; font-size: 24px; font-weight: 700; color: var(--ink); }
  .date { top: 962px; font-size: 25px; font-weight: 700; color: var(--navy); line-height: 37px; }
  .rsvp { top: 1048px; font-size: 17px; font-weight: 700; color: var(--ink); line-height: 24px; }

  .sponsors {
    position: absolute; left: 0; top: 1105px; width: 100%; height: 80px;
  }
  .sponsor {
    position: absolute; top: 0; height: 80px;
    display: flex; align-items: center; gap: 8px;
    font-weight: 700; font-size: 17px; color: var(--rust);
  }
  .sponsor__mark { width: 40px; height: 40px; background: var(--rust); flex: none; }
  .sponsor__mark--round { border-radius: 50%; }
  .sponsor--orrin { left: 80px; }
  .sponsor--halvard { left: 140px; }
  .sponsor--brightmere { left: 318px; }
  .sponsor--velora { left: 480px; }
  .sponsor--tessan { left: 640px; }
</style>
</head>
<body>
  <div class="foliage foliage--top-left" role="img" aria-label="Soft painted leaf sprigs"></div>
  <div class="foliage foliage--top-right" role="img" aria-label="Soft painted leaf sprigs"></div>
  <div class="foliage foliage--left" role="img" aria-label="Soft painted fern fronds"></div>
  <div class="foliage foliage--bottom-right" role="img" aria-label="Soft painted leaf sprigs"></div>
  <div class="foliage foliage--under-frame" role="img" aria-label="Faint leaf branches beneath the photo"></div>

  <h1 class="host">FENWICK PARTNERS</h1>
  <div class="event-title event-title__line--one">Weekend</div>
  <div class="event-title event-title__line--two">Warm Up</div>

  <div class="photo-frame">
    <div class="photo" role="img" aria-label="Venue interior: long dining table with flowers and candles before a lit bar wall of bottles and plants"></div>
    <h2 class="photo__caption">CLIENT<br>APPRECIATION<br>EVENT</h2>
  </div>

  <p class="details venue">The Larkspur Loft</p>
  <p class="details address">482 W Tamsin Ave. Chicago IL 60618</p>
  <p class="details date">Thursday August 23rd, 2018<br>5:30-9:00pm</p>
  <p class="details rsvp">Please RSVP to:<br>gathering@fenwickpartners.com</p>

  <div class="sponsors">
    <div class="sponsor sponsor--orrin"><span class="sponsor__mark"></span></div>
    <div class="sponsor sponsor--halvard">Halvard Hospitality</div>
    <div class="sponsor sponsor--brightmere"><span class="sponsor__mark"></span>Brightmere</div>
    <div class="sponsor sponsor--velora"><span class="sponsor__mark sponsor__mark--round"></span>VELORA</div>
    <div class="sponsor sponsor--tessan"><span class="sponsor__mark"></span>Tessan</div>
  </div>
</body>
</html>
```